Business card design for strategy and management consulting company. Would like to have a clean and professional business card, based on the attached logo. The company is a strategy and management consulting company focusing on sustainable business modlels based on economic, social and environmental market opportunities. Preferably the logo should be included on both sides of the design.

Industry/Entity Type

Business

Contact Information for Business Card

Håvard Lilleby, CEO/Management consultant
havard.lilleby@quarvenpartners.example
Mob: +47 948 26 317
Office: Vikfjell gate 14, pb 312 sentrum, N-0172 Oslo Norway

Requirements
Must have
• Include attached logo
Nice to have
• Would like to have the logo on both sides
Should not have
• Many colours.

```html
<!DOCTYPE html>
<html lang="en">
<head>
<meta charset="utf-8">
<title>Quarven – Business Card</title>
<link rel="stylesheet" href="https://fonts.googleapis.com/css2?family=Open+Sans:wght@400;600;700&display=swap">
<style>
  :root {
    --backdrop: #3a3431;
    --card: #1c1c1c;
    --white: #ffffff;
    --muted: #d6d6d6;
    --accent: #f6e21e;
    --ink: #141414;
    --rule: #555555;
  }
  * { box-sizing: border-box; margin: 0; padding: 0; }
  html, body {
    width: 1200px; height: 764px; overflow: hidden;
    background: var(--backdrop);
    font-family: "Open Sans", Arial, sans-serif;
  }
  .canvas {
    position: relative; width: 1200px; height: 764px;
  }
  .card {
    position: absolute; top: 232px;
    width: 520px; height: 300px;
    background: var(--card);
    box-shadow: 0 14px 30px rgba(0,0,0,.45);
    overflow: hidden;
  }
  .card--front { left: 60px; }
  .card--back  { left: 620px; }

  .brand {
    position: absolute; display: flex; align-items: center; gap: 8px;
    color: var(--white); font-weight: 700; letter-spacing: -0.5px;
    line-height: 1;
  }
  .brand__dot {
    width: 10px; height: 10px; border-radius: 50%;
    background: var(--accent);
  }
  .card--front .brand { left: 0; right: 0; top: 48px; justify-content: center; font-size: 50px; }
  .card--back .brand  { left: 0; right: 0; top: 120px; justify-content: center; font-size: 60px; }

  .divider {
    position: absolute; left: 222px; top: 138px;
    width: 1px; height: 72px; background: var(--rule);
  }
  .person {
    position: absolute; right: 312px; top: 150px; text-align: right;
  }
  .person__name { color: var(--white); font-size: 20px; font-weight: 400; }
  .person__title { color: var(--accent); font-size: 11px; margin-top: 2px; }

  .contact {
    position: absolute; left: 238px; top: 146px;
    list-style: none; display: grid; gap: 10px;
  }
  .contact__item {
    display: flex; align-items: center; gap: 9px;
    color: var(--muted); font-size: 11.5px;
  }
  .contact__icon { width: 13px; height: 13px; flex: none; }

  .address-band {
    position: absolute; left: 0; right: 0; top: 232px; height: 38px;
    background: var(--accent);
    display: flex; align-items: center; padding-left: 30px;
    color: var(--ink); font-size: 15px;
  }
</style>
</head>
<body>
<main class="canvas">
  <section class="card card--front">
    <div class="brand"><span>Quarven</span><span class="brand__dot"></span></div>
    <div class="person">
      <p class="person__name">Håvard Lilleby</p>
      <p class="person__title">CEO/Management consultant</p>
    </div>
    <div class="divider"></div>
    <ul class="contact">
      <li class="contact__item">
        <svg class="contact__icon" viewBox="0 0 13 13"><rect width="13" height="13" rx="1.5" fill="#f6e21e"/><rect x="4" y="2.5" width="5" height="8" rx="0.8" fill="none" stroke="#141414" stroke-width="1"/></svg>
        +47 948 26 317
      </li>
      <li class="contact__item">
        <svg class="contact__icon" viewBox="0 0 13 13"><rect width="13" height="13" rx="1.5" fill="#f6e21e"/><rect x="2.5" y="4" width="8" height="5.5" fill="none" stroke="#141414" stroke-width="1"/><path d="M2.5 4 L6.5 7 L10.5 4" fill="none" stroke="#141414" stroke-width="1"/></svg>
        havard.lilleby@quarvenpartners.example
      </li>
    </ul>
    <div class="address-band">Vikfjell gate 14, pb 312 sentrum, Oslo Norway</div>
  </section>

  <section class="card card--back">
    <div class="brand"><span>Quarven</span><span class="brand__dot"></span></div>
  </section>
</main>
</body>
</html>
```